New management consulting website

I need a 4-5 page website that I can manage in WordPress on Hostlane.example for a new management consulting company. The website is www.torvik-example.com and the company name is Torvik Group LLC. The attached spec has an example of a draft site, layout and actual copy and includes company and contact information. I have more high-res images I can send.

Must include instruction/assistance loading the site to my WordPress dashboard.

Target Market(s)

Any business, especially SAAS

Industry/Entity Type

Consultant

Coding

Coded - Design and coding required

Number of Pages Required

4 page

Font styles to use
Sans Serif

Colors
0456a4

Requirements
Must have
• Modern and stylish

```html
<!DOCTYPE html>
<html lang="en">
<head>
<meta charset="utf-8">
<title>Services – Torvik Consulting</title>
<link href="https://fonts.googleapis.com/css2?family=Lato:wght@400;700&family=Michroma&display=swap" rel="stylesheet">
<style>
:root{
  --navy:#1d3e6c;
  --navy-deep:#1a3a66;
  --text:#4f4f4f;
  --nav:#333333;
  --grey-bg:#f2f2f2;
  --rule:#9a9a9a;
  --footer-bar:#8b8b8b;
  --white:#ffffff;
}
*{margin:0;padding:0;box-sizing:border-box}
html,body{width:1200px;height:2989px;overflow:hidden;background:var(--white)}
body{position:relative;font-family:'Lato',sans-serif;color:var(--text)}
.abs{position:absolute}

/* header */
.site-header{position:absolute;left:0;top:0;width:1200px;height:102px;background:var(--white)}
.brand{position:absolute;left:121px;top:36px;font-family:'Lato',sans-serif;font-weight:700;font-size:26px;color:var(--navy);letter-spacing:1px}
.main-nav{position:absolute;top:49px;left:0;font-size:14px;color:var(--nav)}
.main-nav a{position:absolute;white-space:nowrap;text-decoration:none;color:var(--nav)}
.main-nav a.active{color:var(--navy)}
.main-nav a.active::before{content:"";position:absolute;left:50%;top:-14px;width:22px;height:4px;margin-left:-11px;background:#9a9a9a}
.btn{position:absolute;display:flex;align-items:center;justify-content:center;background:var(--navy);color:var(--white);font-size:14px;text-decoration:none;width:158px;height:44px}

/* hero */
.hero-photo{position:absolute;left:0;top:102px;width:1200px;height:356px;
  clip-path:polygon(0 0,100% 0,100% 100%,0 96%);
  background:
   radial-gradient(ellipse 260px 160px at 230px 330px,rgba(40,44,48,.85),rgba(40,44,48,0) 70%),
   linear-gradient(180deg,#b8c3cb 0%,#dde3e7 45%,#eef1f3 60%,#a9b5bf 100%)}
.hero-title{position:absolute;left:0;width:1200px;top:246px;text-align:center;font-family:'Michroma',sans-serif;font-size:40px;color:var(--navy);letter-spacing:2px}

/* service blocks */
.band-grey{position:absolute;left:0;width:1200px;background:var(--grey-bg)}
.service-photo{position:absolute}
.service-title{position:absolute;font-weight:700;font-size:27px;color:var(--navy-deep)}
.service-rule{position:absolute;width:54px;height:2px;background:var(--rule)}
.service-copy{position:absolute;width:450px;font-size:13.5px;line-height:16.2px;color:var(--text)}
.service-copy p{margin-bottom:16px}

/* footer */
.site-footer{position:absolute;left:0;top:2646px;width:1200px;height:302px;background:var(--navy);color:var(--white)}
.footer-brand{position:absolute;left:93px;top:128px;font-weight:700;font-size:34px;letter-spacing:1px}
.footer-heading{position:absolute;top:72px;font-family:'Michroma',sans-serif;font-size:13px;letter-spacing:.3px}
.footer-heading::after{content:"";position:absolute;left:0;top:26px;width:56px;height:2px;background:#8fa3bf}
.footer-list{position:absolute;list-style:none;font-size:13.5px;line-height:21px}
.contact-item{position:absolute;left:455px;font-size:13.5px;line-height:16px}
.contact-icon{position:absolute;left:424px}
.copyright{position:absolute;left:0;top:2948px;width:1200px;height:41px;background:var(--footer-bar);color:var(--white);font-size:13px;display:flex;align-items:center;justify-content:center}
</style>
</head>
<body>

<header class="site-header">
  <div class="brand">Torvik Consulting</div>
  <nav class="main-nav">
    <a style="left:562px">HOME</a>
    <a style="left:638px">ABOUT</a>
    <a class="active" style="left:719px">SERVICES</a>
    <a style="left:813px">CONTACT</a>
  </nav>
  <a class="btn" style="left:931px;top:35px">GET A QUOTE</a>
</header>

<div class="hero-photo" role="img" aria-label="Hiker standing on a rocky summit above a sea of clouds and distant mountains"></div>
<h1 class="hero-title">SERVICES</h1>

<!-- Strategy & Operation -->
<div class="service-photo" role="img" aria-label="Business team placing sticky notes on a glass wall during a workshop"
  style="left:480px;top:462px;width:720px;height:545px;clip-path:polygon(0 0,100% 2%,100% 95%,0 100%);
  background:linear-gradient(90deg,rgba(255,255,255,1) 0%,rgba(255,255,255,.6) 18%,rgba(150,140,128,.55) 40%,#6d6458 60%,#8a98a8 78%,#5d6e80 100%)"></div>
<h2 class="service-title" style="left:118px;top:584px">Strategy &amp; Operation</h2>
<div class="service-rule" style="left:118px;top:635px"></div>
<div class="service-copy" style="left:118px;top:662px">
  <p>Strategy sets the foundation for a successful and profitable future. At Torvik Consulting, we focus on helping you translate your ideas into implementable and sustainable operational stategies.</p>
  <p>We will work with you to create a customized approach to optimize performance, establish best practice, improve quality and enhance the customer experience.</p>
  <p>Our priority is to help you achieve operational excellence through continuous improvement. We focus on enabling you to consistently deliver quality through lean operations.</p>
</div>
<a class="btn" style="left:118px;top:874px">CONTACT</a>

<!-- Data Analysis & Insights -->
<div class="band-grey" style="top:982px;height:590px;clip-path:polygon(0 5%,100% 0,100% 100%,0 93%)"></div>
<div class="service-photo" role="img" aria-label="Hands over printed charts, graphs and sticky notes spread on a wooden table"
  style="left:0;top:1010px;width:730px;height:545px;clip-path:polygon(0 6%,100% 0,100% 100%,0 91%);
  background:linear-gradient(270deg,rgba(242,242,242,1) 0%,rgba(242,242,242,.5) 18%,rgba(210,200,190,.7) 35%,#b7a796 55%,#7a5f48 80%,#5b4535 100%)"></div>
<h2 class="service-title" style="left:653px;top:1128px">Data Analysis &amp; Insights</h2>
<div class="service-rule" style="left:655px;top:1179px"></div>
<div class="service-copy" style="left:655px;top:1206px;width:430px">
  <p>At Torvik Consulting we are passionate about leveraging the power of data to understand business performance, customer needs and revenue opportunities.</p>
  <p>We will help you identify the&nbsp; key metrics that will offer maximum insight to focus your corporate strategy, optimize your opertions and inform your decision making.</p>
  <p>Torvik Consulting will help you use your data to improve customer engagement, drive new customer acquistion, reduce customer attrition and increase customer satisfaction.</p>
</div>
<a class="btn" style="left:655px;top:1418px">CONTACT</a>

<!-- Leadership Development -->
<div class="service-photo" role="img" aria-label="Presenter in a suit speaking to colleagues at a meeting table"
  style="left:440px;top:1555px;width:760px;height:572px;clip-path:polygon(0 0,100% 6%,100% 100%,0 100%);
  background:linear-gradient(90deg,rgba(255,255,255,1) 0%,rgba(255,255,255,.7) 20%,rgba(225,220,214,.8) 40%,#c8c2ba 58%,#4a5566 72%,#d9d5cf 88%,#7a5a44 100%)"></div>
<h2 class="service-title" style="left:115px;top:1696px">Leadership Development</h2>
<div class="service-rule" style="left:117px;top:1747px"></div>
<div class="service-copy" style="left:117px;top:1774px">
  <p>Achieving exceptional performance and delighting customers is a team effort.</p>
  <p>Torvik Consulting will work with you to understand your leadership development needs and deliver engaging and interactive workshops to drive high performance, motivation and engagement.</p>
  <p>Our workshops will help your current or future leaders to embrace a culture of excellence, achieve peak performance and empower them to create strategies that facilitiate the greater good.</p>
</div>
<a class="btn" style="left:117px;top:1976px">CONTACT</a>

<!-- Executive Leadership -->
<div class="band-grey" style="top:2106px;height:540px;clip-path:polygon(0 4%,100% 0,100% 100%,0 100%)"></div>
<div class="service-photo" role="img" aria-label="Businessman seen from behind blended with a city skyline"
  style="left:0;top:2106px;width:720px;height:540px;clip-path:polygon(0 6%,100% 0,100% 100%,0 100%);
  background:linear-gradient(270deg,rgba(242,242,242,1) 0%,rgba(242,242,242,.5) 20%,#b9c3cf 40%,#2f3f5c 55%,#3c4d6a 68%,#c6cfda 85%,#dde2e8 100%)"></div>
<h2 class="service-title" style="left:660px;top:2257px">Executive Leadership</h2>
<div class="service-rule" style="left:661px;top:2309px"></div>
<div class="service-copy" style="left:661px;top:2336px;width:430px">
  <p>Torvik Consulting can support your business during times of transformational change by providing interim Executive Leadership on a short-term basis.</p>
  <p>We can provide experienced leadership to support you through leadership transitions. Mergers and Acquisitions, restructuning and business turn-arounds. Experts help when you need it, for as long as you need it.</p>
</div>
<a class="btn" style="left:661px;top:2502px">CONTACT</a>

<footer class="site-footer">
  <div class="footer-brand">Torvik Consulting</div>

  <div class="footer-heading" style="left:422px">CONTACT INFO.</div>
  <svg class="contact-icon" style="top:132px" width="14" height="16" viewBox="0 0 14 16"><path d="M7 0a5.5 5.5 0 0 0-5.5 5.5C1.5 9.5 7 16 7 16s5.5-6.5 5.5-10.5A5.5 5.5 0 0 0 7 0zm0 7.6a2.1 2.1 0 1 1 0-4.2 2.1 2.1 0 0 1 0 4.2z" fill="#8fa3bf"/></svg>
  <div class="contact-item" style="top:132px">48 Meridian Row<br>#210, Fairhaven, GA 30999</div>
  <svg class="contact-icon" style="top:186px" width="15" height="11" viewBox="0 0 15 11"><rect x="0" y="0" width="15" height="11" rx="1" fill="#8fa3bf"/><path d="M0.5 0.8 7.5 6 14.5 0.8" stroke="#1d3e6c" stroke-width="1.3" fill="none"/></svg>
  <div class="contact-item" style="top:182px">info@torvik-example.com</div>
  <svg class="contact-icon" style="top:212px" width="16" height="16" viewBox="0 0 16 16"><path d="M3.2 1.2 5.6 3.6 4.4 5.6c.9 2.2 3.2 4.5 6 6l2-1.2 2.4 2.4-1.8 2.2C6.8 14.6 1.4 9.2.9 3z" fill="#8fa3bf"/></svg>
  <div class="contact-item" style="top:214px">Tel: 555-014-0199</div>

  <div class="footer-heading" style="left:733px">QUICK LINKS</div>
  <ul class="footer-list" style="left:733px;top:128px">
    <li>Home</li><li>About</li><li>Services</li><li>Contact</li>
  </ul>

  <div class="footer-heading" style="left:951px">USEFUL LINKS</div>
  <ul class="footer-list" style="left:953px;top:128px">
    <li>Privacy policy</li><li>Terms &amp; conditions</li>
  </ul>
</footer>
<div class="copyright">© 2021 Torvik Group LLC | All Rights Reserved</div>

</body>
</html>
```